ALL TEXT Social Media Graphics

We are looking for a series of social media graphics for Instagram (new size: 4:5 (1080 x 1350 pixels) ratio that are ALL TEXT. We want the following quotes below on each graphic; one quote per graphic. AND, In very small letters at the bottom of each graphic, add @KPBrandellLive
The look and feel of these graphics should be complimentary to the color palette attached below; but keep them simple. But the design is up to you; at the end of this document, I provided various samples of all text graphics that I like as examples.
The Quotes are in the attached WORD document
Target Market(s)
women trying to lose weight
Look and feel
Each slider illustrates characteristics of the customer's brand and the style your logo design should communicate.

```html
<!DOCTYPE html>
<html lang="en">
<head>
<meta charset="utf-8">
<title>Summer Reboot Quote Graphic</title>
<link rel="stylesheet" href="https://fonts.googleapis.com/css2?family=Oswald:wght@600&family=Open+Sans:wght@700&display=swap">
<style>
  :root {
    --magenta: #ad1655;
    --magenta-mid: #d9588a;
    --pink: #ef8fb0;
    --blush: #f8d3df;
    --blush-light: #fdf1f5;
    --white: #ffffff;
    --ink: #000000;
  }
  html, body {
    margin: 0;
    padding: 0;
    width: 960px;
    height: 1200px;
    overflow: hidden;
  }
  .post {
    position: relative;
    width: 960px;
    height: 1200px;
    overflow: hidden;
    background: linear-gradient(180deg,
      var(--magenta) 0%,
      var(--magenta) 14%,
      var(--magenta-mid) 33%,
      var(--pink) 58%,
      var(--blush) 80%,
      var(--blush-light) 94%);
    font-family: "Oswald", "Arial Narrow", sans-serif;
  }
  .headline,
  .subline,
  .call-to-action {
    position: absolute;
    margin: 0;
    font-weight: 600;
    white-space: nowrap;
    transform-origin: left top;
  }
  .headline {
    left: 98px;
    top: 96px;
    color: var(--white);
    font-size: 97px;
    line-height: 98px;
    text-transform: uppercase;
    letter-spacing: -0.5px;
    transform: scaleX(0.82);
  }
  .subline {
    left: 98px;
    top: 473px;
    color: var(--ink);
    font-size: 110px;
    line-height: 98px;
    letter-spacing: -1px;
    transform: scaleX(0.76);
  }
  .call-to-action {
    left: 185px;
    top: 912px;
    color: var(--magenta);
    font-size: 64px;
    line-height: 63px;
    text-transform: uppercase;
    letter-spacing: -0.5px;
    transform: scaleX(0.78);
  }
  .handle-band {
    position: absolute;
    left: 0;
    bottom: 0;
    width: 960px;
    height: 78px;
    background: linear-gradient(90deg,
      var(--blush-light) 0%,
      #d9679a 22%,
      var(--magenta) 50%,
      #d9679a 78%,
      var(--blush-light) 100%);
    display: flex;
    align-items: center;
    justify-content: center;
  }
  .handle {
    color: var(--white);
    font-family: "Open Sans", Arial, sans-serif;
    font-weight: 700;
    font-size: 29px;
    letter-spacing: -0.3px;
  }
</style>
</head>
<body>
  <main class="post">
    <h1 class="headline">You can absolutely<br>be down 20–30 pounds<br>by end of summer.</h1>
    <p class="subline">All it Takes is<br>The Right Plan—and<br>You've Found it.</p>
    <p class="call-to-action">Comment “Bright Me” for the<br>Bright Me Summer Reboot!</p>
    <footer class="handle-band">
      <span class="handle">@KPBrandellLive</span>
    </footer>
  </main>
</body>
</html>
```